Pull Up Banner Design 85cm X200cm

The pull up banner is intended for branding and services awareness purposes, and to be used at exhibition and conference. Please refer to the websites below for more information
1. https://www.advisory-nook.net/
2. https://www.advisory-nook.net/landing-page
3. https://blog.advisory-nook.net/faq-for-client/
4. https://blog.advisory-nook.net/faq-for-advisor/

Ideally, the banner will lead potential users both young entrepreneurs and online business owners (as clients) to Brivana Hub marketplace, and also professional services providers like accountants and finance advisors and consultants (as advisors) to sign up with the platform. (Like ArtForge marketplace)

Target Market(s)

Business users and accountants aged between 25 to 44 yrs old

Requirements
Must have
• website address (www.advisory-nook.net)
• and
• company logo "Brivana Hub" as attached

```html
<!DOCTYPE html>
<html lang="en">
<head>
<meta charset="utf-8">
<title>Brivana Hub Pull Up Banner</title>
<link href="https://fonts.googleapis.com/css2?family=Questrial&family=Oswald:wght@400;600&family=Nunito:wght@400;700;800&display=swap" rel="stylesheet">
<style>
  :root {
    --stage: #e9eaec;
    --paper: #ffffff;
    --brand-blue: #1a6fc0;
    --bright-blue: #2c95e0;
    --light-blue: #4aa8ea;
    --ink: #3d3f44;
    --ink-soft: #55585e;
    --faint: #c9ccd1;
    --rule: #45474c;
  }
  html, body { margin: 0; padding: 0; width: 1200px; height: 1200px; overflow: hidden; background: var(--stage); }
  .banner {
    position: absolute; left: 348px; top: 30px; width: 504px; height: 1140px;
    background: var(--paper); overflow: hidden;
    font-family: "Questrial", sans-serif; color: var(--ink);
  }
  .banner-art { position: absolute; inset: 0; }
  .top-brand { position: absolute; left: 0; width: 100%; top: 60px; text-align: center; }
  .top-brand .mark { width: 60px; height: 60px; border-radius: 50%; background: #dcdee2; margin: 0 auto 12px; }
  .top-brand .name { font-family: "Nunito", sans-serif; font-weight: 700; font-size: 36px; color: var(--faint); }
  .main-brand { position: absolute; right: 32px; top: 582px; text-align: right; }
  .main-brand .mark { width: 68px; height: 68px; border-radius: 50%; background: var(--brand-blue); margin-left: auto; margin-right: 56px; }
  .main-brand .name { font-family: "Nunito", sans-serif; font-weight: 800; font-size: 38px; color: var(--brand-blue); margin-top: 6px; }
  .services { position: absolute; left: 34px; top: 728px; font-size: 19px; line-height: 27px; color: var(--ink-soft); text-transform: uppercase; letter-spacing: -0.2px; }
  .headline { position: absolute; left: 34px; top: 784px; width: 440px; font-family: "Oswald", sans-serif; text-transform: uppercase; color: var(--ink-soft); }
  .headline .line-one { font-weight: 600; font-size: 31px; line-height: 40px; letter-spacing: -0.3px; }
  .headline .line-two { font-weight: 400; font-size: 27px; line-height: 36px; }
  .headline .accent { color: var(--brand-blue); }
  .headline .accent-bright { color: var(--bright-blue); font-weight: 600; }
  .faq-box { position: absolute; left: 34px; top: 871px; width: 426px; height: 92px; border: 1.5px solid #77797e; box-sizing: border-box; text-align: center; }
  .faq-box .title { font-family: "Questrial", sans-serif; font-size: 26px; margin-top: 12px; color: var(--ink); }
  .faq-box .audience { display: flex; align-items: center; justify-content: center; gap: 8px; margin-top: 4px; font-family: "Nunito", sans-serif; font-weight: 800; font-size: 26px; color: var(--bright-blue); }
  .faq-box .audience::before, .faq-box .audience::after { content: ""; width: 100px; height: 1.5px; background: var(--rule); }
  .contact { position: absolute; right: 26px; top: 1032px; text-align: right; color: #fff; font-family: "Nunito", sans-serif; }
  .contact .cta { font-weight: 800; font-size: 20px; letter-spacing: 0.3px; border-bottom: 2px solid #fff; padding-bottom: 2px; }
  .contact .detail { font-size: 15px; line-height: 18px; margin-top: 4px; }
  .contact .social { display: flex; justify-content: flex-end; gap: 6px; margin-top: 5px; }
  .contact .social span { width: 20px; height: 20px; border-radius: 50%; background: #fff; display: block; }
  .website { position: absolute; left: 46px; top: 1104px; color: #fff; font-family: "Nunito", sans-serif; font-size: 20px; }
  .website b { font-weight: 800; }
</style>
</head>
<body>
<div class="banner">
  <svg class="banner-art" width="504" height="1140" viewBox="0 0 504 1140">
    <defs>
      <linearGradient id="photoTone" x1="0" y1="0" x2="0" y2="1">
        <stop offset="0" stop-color="#ffffff"/>
        <stop offset="0.25" stop-color="#c9d6e4"/>
        <stop offset="0.6" stop-color="#5b7a9e"/>
        <stop offset="1" stop-color="#24406a"/>
      </linearGradient>
      <linearGradient id="footerBlue" x1="0" y1="0" x2="1" y2="1">
        <stop offset="0" stop-color="#2b8fdc"/>
        <stop offset="1" stop-color="#1766b4"/>
      </linearGradient>
    </defs>
    <polygon role="img" aria-label="Photo of a presenter speaking to a seated business audience" fill="url(#photoTone)" points="0,300 504,300 504,406 184,598 0,489"/>
    <polygon fill="#1a6fc0" points="0,489 184,598 504,406 504,470 158,664 0,578"/>
    <polyline fill="none" stroke="#45474c" stroke-width="6" points="0,592 152,680 504,488"/>
    <polygon fill="#45474c" points="0,1102 345,980 504,1034 504,1044 345,990 0,1112"/>
    <polygon fill="url(#footerBlue)" points="0,1110 345,988 504,1042 504,1140 0,1140"/>
    <polygon fill="#4aa8ea" points="0,984 176,1042 0,1104"/>
  </svg>

  <div class="top-brand">
    <div class="mark"></div>
    <div class="name">Brivana Hub</div>
  </div>

  <div class="main-brand">
    <div class="mark"></div>
    <div class="name">Brivana Hub</div>
  </div>

  <div class="services">Tax, Accounting, Financials,<br>Business Advisory, Fundraising Services</div>

  <div class="headline">
    <div class="line-one"><span class="accent">Brivana Hub</span> matches you with</div>
    <div class="line-two">The right advisors <span class="accent-bright">online!</span></div>
  </div>

  <div class="faq-box">
    <div class="title">Frequently Asked Questions</div>
    <div class="audience">For Clients</div>
  </div>

  <div class="contact">
    <div class="cta">GET IN TOUCH WITH US</div>
    <div class="detail">Contact &amp; Customer Support<br>Follow Us On</div>
    <div class="social"><span></span><span></span></div>
  </div>

  <div class="website">www.<b>advisory-nook</b>.net</div>
</div>
</body>
</html>
```